Norwegian Mobile Home/Cabin Producer Needs Brochure Design

We make and deliver our own brand of mobile homes especially made for Norway and it's weather conditions. We differ from other brands in building quality in regards to a much more solid construction, insulation and choices. We work with our customer from the beginning and build them after their demands and wishes.
We need a brochure that holds us out as top of the line. We deliver mobile homes of all kinds and sizes. Both to the private and professional sector.
For the professional sector, mainly camping sites we want to show, lodges-, sanitary- and kitchen wagoons etc.
So we need a brochure of 14-20 pages in A4 where the double pages can be printed in A3 format.
We have logo (provided). But we need cover as well as back suggestions.
It should start with pages where we can teel who we are and stand for.Piicture(s) and space for some editable text (which we can write in norwegian). The text part can have a transparent background......or not. Give us your best shot. Also a smaller part in the private sector that shows winter time.
We want other pages for the private sector that shows what we deliver and the possibilities of choices.
Pages for the the professional sector.
Pages that show our production. How we transport. And the split construction. Only pictures from this portfolio here. (see fotoskap portfolios)
Take a look at provided pictures and our website www.solvikhytta.no for inspiration.
Here's a FotoSkap link to Pictures to choose from. http://bildelagr.example/K4TQ9P
(Hope it Works, let me know if not)
Our company name in small letters "fjordgrønn hyttebygg" means directly translated "fjordgreen cabin builds".
Looking forward to your suggestions.
Target Market(s)
Private market for vacation mobile homes. Camping sites and similar
Industry/Entity Type
Insulation
Requirements
Must have
- Our logo on the front page. Simple but inviting and professional
Logo and address on the back.

```html
<!DOCTYPE html>
<html lang="no">
<head>
<meta charset="utf-8">
<title>Professional Sector – brosjyreoppslag</title>
<link rel="stylesheet" href="https://fonts.googleapis.com/css2?family=Source+Sans+3:wght@400;600;700&display=swap">
<style>
  :root{
    --backdrop:#c6c6c6;
    --paper:#ffffff;
    --olive:#7a8b2c;
    --slate:#3b4348;
    --rule:#2d3e5c;
    --mist:#d6d8d9;
    --ink:#2a2a2a;
  }
  *{margin:0;padding:0;box-sizing:border-box}
  html,body{width:1200px;height:800px;overflow:hidden}
  body{background:var(--backdrop);font-family:"Source Sans 3",sans-serif;position:relative}
  .spread{position:absolute;left:20px;top:180px;width:1160px;height:440px;display:flex}
  .page{position:relative;background:var(--paper);height:100%}
  .page--left{width:587px}
  .page--right{width:573px}
  .abs{position:absolute}
  .section-title{left:22px;top:38px;font-size:34px;font-weight:700;color:var(--olive);letter-spacing:.2px;line-height:1}
  .title-rule{left:22px;top:78px;width:538px;height:1px;background:var(--rule)}
  .section-sub{left:63px;top:84px;font-size:10px;font-weight:700;color:var(--olive);letter-spacing:.2px}
  .side-band{left:0;top:115px;width:83px;height:252px;background:var(--slate)}
  .photo{background:linear-gradient(180deg,#b9c4cc 0%,#dfe3e4 45%,#7d8a6f 78%,#4a4d49 100%)}
  .hero-photo{left:83px;top:115px;width:477px;height:252px}
  .folio{font-size:6px;font-weight:700;color:var(--ink);top:412px}
  .folio--left{left:22px}
  .folio--right{right:28px}

  .thumb-photo{left:9px;top:22px;width:164px;height:99px;background:linear-gradient(160deg,#e4e4e2,#9c9a95 70%,#6d6a66)}
  .chapter-box{left:173px;top:22px;width:359px;height:92px;background:var(--olive);color:#fff}
  .chapter-num{position:absolute;left:21px;top:16px;font-size:28px;font-weight:700;line-height:1}
  .chapter-rule{position:absolute;left:21px;top:56px;width:338px;height:1px;background:rgba(255,255,255,.75)}
  .chapter-sub{position:absolute;left:21px;top:61px;font-size:10px;font-weight:700;letter-spacing:.2px}
  .edge-tab{left:532px;top:79px;width:25px;height:37px;background:var(--slate)}
  .text-panel{left:9px;top:125px;width:164px;height:212px;background:var(--olive);color:#e9eed6;font-size:6px;text-align:right;padding:26px 12px 0 8px;line-height:20px}
  .text-panel p+p{margin-top:14px}
  .text-panel strong{font-weight:600;color:#fff}
  .bath-photo{left:173px;top:116px;width:129px;height:221px;background:linear-gradient(180deg,#d9d9d6 0%,#a6a49f 55%,#5f5d5a 100%)}
  .kitchen-photo{left:309px;top:116px;width:223px;height:221px;background:linear-gradient(180deg,#eeeeec 0%,#d6d5d2 60%,#6d645b 100%)}
  .mist-bar{left:9px;top:337px;width:548px;height:32px;background:var(--mist)}
  .caption-box{left:364px;top:337px;width:168px;height:29px;background:var(--slate);color:#e5e7e8;font-size:7px;padding:9px 0 0 10px;letter-spacing:.1px}
  .caption-box b{font-weight:700;color:#fff;margin-right:2px}
  .foot-band{left:173px;top:369px;width:359px;height:28px;background:var(--olive)}
</style>
</head>
<body>
  <main class="spread">
    <section class="page page--left">
      <h1 class="abs section-title">PROFESSIONAL SECTOR</h1>
      <div class="abs title-rule"></div>
      <p class="abs section-sub">TEM QUATIAM SEPSANT HILIS VOLUMER NOTUS MODU VISTA</p>
      <div class="abs side-band"></div>
      <div class="abs photo hero-photo" role="img" aria-label="Hvit mobil hytte med store glassvinduer og belyste plantekrukker i skumring"></div>
      <span class="abs folio folio--left">4</span>
    </section>

    <section class="page page--right">
      <div class="abs thumb-photo" role="img" aria-label="Kjøkkenbenk med vask, krydderplante og glass mot flislagt vegg"></div>
      <header class="abs chapter-box">
        <span class="chapter-num">01</span>
        <span class="chapter-rule"></span>
        <span class="chapter-sub">TEM QUATIAM SEPSANT HILIS VOLUMER NOTUS MODU VISTA</span>
      </header>
      <div class="abs edge-tab"></div>
      <div class="abs text-panel">
        <p>Ibusamus, ibusaestist, sit magni<br>quat. Lora dolorem eumtem perspera<br>sunt magnatur cum ventus, omnis<br>cust, quae cumdae sunt, nost.</p>
        <p>Ostio exped quas <strong>sequamus, sam</strong><br><strong>faccae eum</strong> sitiore sit et, si arum sam<br>dolecum eada nos, orearit, sust, num</p>
      </div>
      <div class="abs bath-photo" role="img" aria-label="Baderom med vegghengt toalett, grå fliser og dusjkabinett"></div>
      <div class="abs kitchen-photo" role="img" aria-label="Hvitt kjøkken med ventilator, stekeovn og benkeplate i tre"></div>
      <div class="abs mist-bar"></div>
      <div class="abs caption-box"><b>01</b>TEM QUATIAM SEPSANT HILIS</div>
      <div class="abs foot-band"></div>
      <span class="abs folio folio--right">5</span>
    </section>
  </main>
</body>
</html>
```